Anzeigengestaltung für Wochenblatt
Zielgruppe
Wir bieten professionelle Schädlingsbekämpfung an. Unsere Zielgruppe sind Privathaushalte, aber auch Gewerbekunden mit Schädlingsproblemen. Zu den hauptsächlichen Schädlingen zählen Mäuse, Ratten, Wespen, Schaben, Silberfische, Ameisen sowie verschiedene weitere Insekten (Käfer, Fliegen usw.)
Aufgabenstellung
Es sollten verschiedene Vorlagen erstellt werden, da die Schädlinge je nach Jahreszeit auftreten. Im Frühjahr/Sommer sind es vermehrt Wespen, Ameisen und Insekten, im Herbst/Winter vermehrt Ratten/Mäuse
Für Wespen speziell hätten wir gerne eine Anzeige als "Wespen-Notruf" mit unserer Telefon-Nummer und der Internetadresse www.plagenfrei-team.example
Die Anzeige soll 1-oder 2-spaltig erscheinen und bunt sein. Die Höhe sollte nicht ins unendliche gehen, da jeder mm Geld kostet, hier sollten also die Informationen kurz und knapp dargelegt werden. Unser Logo sollte am unteren Rand enthalten sein.

```html
<!DOCTYPE html>
<html lang="de">
<head>
<meta charset="utf-8">
<title>Wespen-Notruf Anzeige</title>
<link href="https://fonts.googleapis.com/css2?family=Archivo+Black&family=Arimo:wght@700&display=swap" rel="stylesheet">
<style>
  :root {
    --page: #ffffff;
    --frame: #9a9a9a;
    --yellow: #ffcb05;
    --black: #0a0a0a;
    --red: #c4120f;
    --white: #ffffff;
    --green: #4c9a1f;
    --wasp-dark: #2c2a22;
    --wasp-yellow: #e8c21a;
  }
  html, body {
    margin: 0;
    padding: 0;
    width: 848px;
    height: 1200px;
    overflow: hidden;
    background: var(--page);
  }
  .ad {
    position: absolute;
    left: 309px;
    top: 211px;
    width: 177px;
    height: 444px;
    border: 1px solid var(--frame);
    background: var(--white);
    overflow: hidden;
    font-family: "Arimo", Arial, sans-serif;
  }
  .headline {
    position: absolute;
    left: 0; top: 0;
    width: 100%;
    height: 97px;
    background: var(--yellow);
    margin: 0;
    font-family: "Archivo Black", "Arial Black", sans-serif;
    font-size: 28px;
    line-height: 33px;
    color: var(--black);
    text-align: center;
    padding-top: 14px;
    box-sizing: border-box;
    letter-spacing: 0.2px;
  }
  .wasp-photo {
    position: absolute;
    left: 44px;
    top: 112px;
    width: 133px;
    height: 102px;
    border-radius: 45% 0 0 40%;
    background: linear-gradient(100deg, var(--wasp-dark) 0%, var(--wasp-yellow) 45%, var(--wasp-dark) 65%, var(--wasp-yellow) 100%);
    opacity: 0.85;
  }
  .help-tag {
    position: absolute;
    left: 21px;
    top: 200px;
    width: 122px;
    height: 36px;
    background: var(--red);
    border-radius: 6px;
    transform: rotate(-4deg);
    color: var(--white);
    font-size: 15px;
    line-height: 36px;
    text-align: center;
  }
  .help-arrow {
    position: absolute;
    left: 58px;
    top: 233px;
  }
  .hotline-label {
    position: absolute;
    left: 5px;
    top: 248px;
    width: 162px;
    height: 30px;
    background: var(--yellow);
    transform: rotate(-4deg);
    color: var(--black);
    font-size: 15px;
    line-height: 34px;
    text-align: center;
  }
  .hotline-number {
    position: absolute;
    left: 8px;
    top: 276px;
    width: 162px;
    height: 30px;
    background: var(--black);
    transform: rotate(-4deg);
    color: var(--white);
    font-size: 16px;
    line-height: 30px;
    text-align: center;
  }
  .website {
    position: absolute;
    left: 4px;
    top: 310px;
    width: 172px;
    transform: rotate(-4deg);
    color: var(--black);
    font-size: 9.5px;
    text-align: center;
  }
  .brand {
    position: absolute;
    left: 0;
    top: 370px;
    width: 100%;
    display: flex;
    align-items: center;
    justify-content: center;
    gap: 6px;
    color: var(--green);
    font-size: 24px;
  }
  .brand-dot {
    width: 14px;
    height: 14px;
    border-radius: 50%;
    background: var(--green);
  }
</style>
</head>
<body>
  <div class="ad">
    <h1 class="headline">WESPEN-<br>ALARM?</h1>
    <div class="wasp-photo" role="img" aria-label="Nahaufnahme einer Wespe"></div>
    <div class="help-tag">WIR HELFEN!</div>
    <svg class="help-arrow" width="50" height="22" viewBox="0 0 50 22" aria-hidden="true">
      <polygon points="0,2 50,0 26,20" fill="#c4120f"/>
    </svg>
    <div class="hotline-label">WESPENNOTRUF</div>
    <div class="hotline-number">(01234) 567 00 00</div>
    <div class="website">www.plagenfrei-team.example</div>
    <div class="brand"><span class="brand-dot"></span><span class="brand-name">Kernmann</span></div>
  </div>
</body>
</html>
```